International Vacuum Business Needs a Business Card

We need a business card design for a new company based in Toronto called "Plumora-Sweep". We will be selling and installing a proprietary central vacuum system that is one of a kind to the condominium market mainly through various large builders throughout the country as well as a second distribution chain at a retail level. Our product has a very unique retractable hose system that allows the hose to be stored away within the walls of a space all by the push of a button. "No more hoses laying around the house" We would like to see the design use the colours Red, Black, Grey and possibly white. The design should communicate the following terms " sleek, discreet, convenient, sophisticated, modern"
Updates

Project Deadline Extended
Reason: Hello All, I have not been able to provide very much feedback as I have been unavailable this week so we will be extending the deadline for another 3 days. Thanks,

Project Deadline Extended
Reason: Hello All, The revision and feedback process has been slow so I have no choice but to extend once again. We are still looking for that one great design. Thank you

Project Deadline Extended
Reason: Guys the feedback and changes on some of the designs are taking really long from some of you so I have no choice but to continue extending the deadline forward.

Target Market(s)

Our target market is male/female aged 25-65, more so focussing on 25-50.

Industry/Entity Type

Retail

Requirements
Must have
• Phone #
Fax #
Mobile #
Toll Free #
Web site address "www.plumorasweep.ca"

```html
<!DOCTYPE html>
<html lang="en">
<head>
<meta charset="utf-8">
<title>Plumora-Sweep Business Card</title>
<link href="https://fonts.googleapis.com/css2?family=Montserrat:wght@400;600;700&display=swap" rel="stylesheet">
<style>
  :root {
    --backdrop: #9a9a9a;
    --card-black: #0d0d0d;
    --card-white: #ffffff;
    --accent-red: #b0121b;
    --muted-grey: #cfcfcf;
  }
  * { margin: 0; padding: 0; box-sizing: border-box; }
  html, body {
    width: 1200px;
    height: 1200px;
    overflow: hidden;
    background: var(--backdrop);
    font-family: "Montserrat", sans-serif;
  }
  .sheet {
    position: relative;
    width: 1200px;
    height: 1200px;
  }
  .card {
    position: absolute;
    left: 150px;
    width: 900px;
    height: 514px;
    background: var(--card-black);
    color: var(--card-white);
    box-shadow: 0 6px 18px rgba(0,0,0,0.25);
  }
  .card--back { top: 56px; }
  .card--front { top: 630px; }

  /* back side */
  .back-brand {
    position: absolute;
    inset: 0;
    display: flex;
    align-items: center;
    justify-content: center;
    gap: 26px;
  }
  .back-brand__square {
    width: 70px;
    height: 70px;
    background: var(--card-white);
  }
  .back-brand__name {
    font-size: 64px;
    font-weight: 400;
    letter-spacing: 1px;
  }

  /* front side */
  .brand {
    position: absolute;
    left: 48px;
    top: 118px;
  }
  .brand__lockup {
    display: flex;
    align-items: center;
    gap: 14px;
  }
  .brand__square {
    width: 40px;
    height: 40px;
    background: var(--card-white);
  }
  .brand__name {
    font-size: 50px;
    font-weight: 400;
    letter-spacing: 1px;
    line-height: 1;
  }
  .brand__tagline {
    margin-top: 30px;
    font-size: 21px;
    font-weight: 600;
  }

  .person {
    position: absolute;
    right: 70px;
    top: 150px;
  }
  .person__name {
    font-size: 32px;
    font-weight: 400;
    line-height: 1;
  }
  .person__name strong { font-weight: 700; }
  .person__role {
    font-size: 14px;
    color: var(--muted-grey);
    margin-top: 2px;
  }

  .contact {
    position: absolute;
    left: 560px;
    top: 344px;
    list-style: none;
    font-size: 22px;
    line-height: 33px;
  }
  .contact__label {
    color: var(--accent-red);
    font-weight: 700;
    display: inline-block;
    width: 30px;
  }
</style>
</head>
<body>
  <main class="sheet">
    <section class="card card--back" aria-label="Card back">
      <div class="back-brand">
        <span class="back-brand__square"></span>
        <span class="back-brand__name">Plumora-Sweep</span>
      </div>
    </section>

    <section class="card card--front" aria-label="Card front">
      <div class="brand">
        <div class="brand__lockup">
          <span class="brand__square"></span>
          <span class="brand__name">Plumora-Sweep</span>
        </div>
        <p class="brand__tagline">no more hoses laying around the house</p>
      </div>

      <div class="person">
        <p class="person__name"><strong>John</strong>Doe</p>
        <p class="person__role">manager</p>
      </div>

      <ul class="contact">
        <li><span class="contact__label">P:</span> 555010232</li>
        <li><span class="contact__label">F:</span> 55501187</li>
        <li><span class="contact__label">M:</span> 55504362</li>
        <li><span class="contact__label">W:</span> www.plumorasweep.ca</li>
      </ul>
    </section>
  </main>
</body>
</html>
```